Seafood restaurant menu

I am looking for a new menu design for my cajun seafood restaurant. I want something modern and simple. Our menu is very small so just one page front and back. Preferred, menu size is (4.25"x11"), I have attach some images, but we will have more to give.
Updates

Need to give designer more time

Target Market(s)

young to middle aged customers

Industry/Entity Type

Restaurant Food industry

Colors
EB3D1F
EC4F4E
F09395
F8D3D4
FCEDEE

Requirements
Must have
• creativity and interesting
Nice to have
• I would like to see a clean and simple menu, but with good color placement and photos of the dishes

```html
<!DOCTYPE html>
<html lang="en">
<head>
<meta charset="utf-8">
<title>Gulf Pot Boil – Seafood Menu</title>
<link href="https://fonts.googleapis.com/css2?family=Antonio:wght@300;400&family=Fraunces:opsz,wght@9..144,600&family=Outfit:wght@400&family=EB+Garamond:ital@1&display=swap" rel="stylesheet">
<style>
:root{
  --red:#E8401F;
  --navy:#1C2A4E;
  --salmon:#F9AE98;
  --salmon-soft:rgba(249,174,152,.45);
  --peach:#F6B487;
  --cream:#F7E7B8;
  --white:#FFFFFF;
}
*{margin:0;padding:0;box-sizing:border-box}
html,body{width:1200px;height:1200px;overflow:hidden;background:var(--white)}
body{position:relative;font-family:'Outfit',sans-serif;color:var(--navy)}
.panel{position:absolute;width:308px;height:797px;background:var(--white);box-shadow:0 4px 14px rgba(0,0,0,.18);overflow:hidden}
.panel--front{left:262px;top:204px}
.panel--back{left:637px;top:206px}
.panel > *{z-index:1}
.header{position:absolute;left:0;top:0;width:100%;height:130px;background:var(--red)}
.header__title{position:absolute;left:15px;top:10px;font-family:'Antonio',sans-serif;font-weight:300;font-size:60px;line-height:55px;color:var(--white);transform:scaleX(.72);transform-origin:left top;white-space:nowrap}
.header__crab{position:absolute;left:101px;top:80px;width:44px;height:34px;border-radius:50%;background:var(--cream)}
.brand{position:absolute;left:193px;top:15px;width:100px;height:100px;border-radius:50%;background:var(--white);display:flex;align-items:center;justify-content:center;text-align:center;font-family:'Outfit',sans-serif;font-size:14px;line-height:16px;color:var(--red)}
.panel > .deco-crab{position:absolute;z-index:0;background:radial-gradient(ellipse at 70% 50%,var(--salmon-soft),rgba(249,174,152,.15) 70%,rgba(249,174,152,0))}
.deco-crab--front{left:180px;top:346px;width:128px;height:238px}
.deco-crab--back{left:0;top:391px;width:66px;height:124px;background:radial-gradient(ellipse at 10% 50%,var(--salmon-soft),rgba(249,174,152,.12) 70%,rgba(249,174,152,0))!important}
.mini-crab{position:absolute;left:13px;top:690px;width:40px;height:36px;border-radius:50%;background:var(--salmon-soft)}
.waves{position:absolute;left:0;top:745px;width:308px;height:52px}
h2{position:absolute;left:0;right:0;text-align:center;font-family:'Fraunces',serif;font-weight:600;font-size:22px;line-height:26px;color:var(--navy);letter-spacing:.5px}
.note{position:absolute;left:8px;right:8px;text-align:center;font-family:'EB Garamond',serif;font-style:italic;font-size:9px;line-height:11px;white-space:nowrap}
.row{position:absolute;left:37px;right:38px;display:flex;font-size:15.5px;line-height:18px;white-space:nowrap;color:var(--navy)}
.row .lead{flex:1;overflow:hidden}
.row .lead::after{content:"........................................................................................"}
.panel--back .row{left:34px;right:31px;font-size:14px}
.panel--back .row.tight{left:31px;right:26px;font-size:11.5px}
.sub{position:absolute;left:31px;right:26px;font-family:'EB Garamond',serif;font-style:italic;font-size:7.5px;line-height:10px;text-align:justify;text-align-last:justify}
.center{position:absolute;left:0;right:0;text-align:center;font-size:14px;line-height:17px}
.photo{position:absolute;top:29px;height:70px}
.photo--1{left:19px;width:91px;background:linear-gradient(135deg,#C8502A,#E7884C 55%,#8E3A22)}
.photo--2{left:126px;width:59px;background:linear-gradient(135deg,#B9472A,#D9753E 55%,#7A3320)}
.photo--3{left:201px;width:88px;background:linear-gradient(135deg,#A8392A,#D86A3A 55%,#6E2C21)}
.caption{position:absolute;top:104px;font-family:'EB Garamond',serif;font-style:italic;font-size:9px;line-height:10px;text-align:center}
</style>
</head>
<body>

<section class="panel panel--front">
  <div class="deco-crab deco-crab--front" role="img" aria-label="Large faint crab illustration"></div>

  <div class="header">
    <div class="header__title">SEAFOOD<br>MENU</div>
    <div class="header__crab" role="img" aria-label="Small crab illustration"></div>
    <div class="brand">Gulf Pot<br>Boil</div>
  </div>

  <h2 style="top:139px">Appetizer</h2>
  <div class="row" style="top:174px"><span>A1. 8pc. Wings</span><span class="lead"></span><span>14/8pc</span></div>
  <div class="note" style="top:194px">(Honey Lemon Pepper/Buffalo/Skipper's Bomb)</div>
  <div class="row" style="top:207px"><span>A2. Garlic Noodles</span><span class="lead"></span><span>7</span></div>

  <h2 style="top:238px">Fried Seafood Baskets</h2>
  <div class="note" style="top:265px">(All baskets served with a side. Sweet Potato Fries or Hush Puppies +1)</div>
  <div class="row" style="top:285px"><span>F1. Fried Oysters</span><span class="lead"></span><span>12</span></div>
  <div class="row" style="top:304px"><span>F2. Fried Shrimp</span><span class="lead"></span><span>13</span></div>
  <div class="row" style="top:323px"><span>F3. Fried Catfish</span><span class="lead"></span><span>12</span></div>
  <div class="row" style="top:342px"><span>F4. Fried Calamari</span><span class="lead"></span><span>12</span></div>
  <div class="row" style="top:362px"><span>F5. Soft Shell Crab *</span><span class="lead"></span><span>15</span></div>

  <h2 style="top:392px">Sides</h2>
  <div class="row" style="top:427px"><span>S1. Cajun Fries</span><span class="lead"></span><span>5</span></div>
  <div class="row" style="top:446px"><span>S2. Sweet Potato Fries</span><span class="lead"></span><span>6</span></div>
  <div class="row" style="top:466px"><span>S3. Hush Puppies</span><span class="lead"></span><span>6</span></div>
  <div class="row" style="top:485px"><span>S4. Coleslaw</span><span class="lead"></span><span>4</span></div>
  <div class="row" style="top:505px"><span>S5. Steamed Rice</span><span class="lead"></span><span>3</span></div>

  <h2 style="top:536px">Extras</h2>
  <div class="row" style="top:572px"><span>E1. Potatoes (3pc)</span><span class="lead"></span><span>$3</span></div>
  <div class="row" style="top:591px"><span>E2. Corn on the cob(2pc)</span><span class="lead"></span><span>$3</span></div>
  <div class="row" style="top:610px"><span>E3. Boiled Eggs (2pc)</span><span class="lead"></span><span>$3</span></div>
  <div class="row" style="top:630px"><span>E4. Sausage....$5 ½LB / $9 1Lb</span></div>
  <div class="row" style="top:649px"><span>E5. Sauce</span><span class="lead"></span><span>$6/Cup</span></div>

  <div class="mini-crab" role="img" aria-label="Small crab illustration"></div>

  <svg class="waves" viewBox="0 0 308 52" preserveAspectRatio="none" aria-hidden="true">
    <path d="M0 4 Q38 2 77 20 Q115 36 154 18 Q192 0 231 18 Q270 36 308 2 V52 H0Z" fill="var(--peach)"/>
    <path d="M0 26 Q38 8 77 16 Q115 24 154 12 Q192 0 231 16 Q270 32 308 8 V52 H0Z" fill="var(--white)"/>
    <path d="M0 30 Q38 10 77 20 Q115 30 154 16 Q192 2 231 20 Q270 36 308 12 V52 H0Z" fill="var(--red)"/>
  </svg>
</section>

<section class="panel panel--back">
  <div class="deco-crab deco-crab--back" role="img" aria-label="Large faint crab illustration"></div>

  <div class="photo photo--1" role="img" aria-label="Photo of a crab plate with snow crab legs and corn"></div>
  <div class="photo photo--2" role="img" aria-label="Photo of a seafood deluxe platter"></div>
  <div class="photo photo--3" role="img" aria-label="Photo of a small crab and sausage boil"></div>
  <div class="caption" style="left:19px;width:91px">Crab Plate2</div>
  <div class="caption" style="left:116px;width:79px">Seafood Deluxe<br>Smaller</div>
  <div class="caption" style="left:201px;width:88px;top:102px">Marina Small</div>

  <h2 style="top:131px">Seafood by the LB</h2>
  <div class="row" style="top:164px"><span>L1. Crawfish</span><span class="lead"></span><span>18</span></div>
  <div class="row" style="top:182px"><span>L2. Shrimp w/ head</span><span class="lead"></span><span>18</span></div>
  <div class="row" style="top:199px"><span>L3. Shrimp w/o head deveined</span><span class="lead"></span><span>20</span></div>
  <div class="row" style="top:215px"><span>L4. Clams</span><span class="lead"></span><span>18</span></div>
  <div class="row" style="top:232px"><span>L5. Mussels</span><span class="lead"></span><span>18</span></div>
  <div class="row" style="top:249px"><span>L6. Snow Crab legs</span><span class="lead"></span><span>39</span></div>
  <div class="row" style="top:266px"><span>L7. Lobster tail</span><span class="lead"></span><span>Seasonal</span></div>
  <div class="row" style="top:283px"><span>L8. King Crab Legs</span><span class="lead"></span><span>Seasonal</span></div>

  <h2 style="top:319px">Seafood Plates</h2>
  <div class="note" style="top:345px">(All plates come with 1 flavor, 1 Corn, Sausages, and 1 Potato)</div>
  <div class="row tight" style="top:364px"><span>P1. Seafood plate 2 LB (1 flavor)</span><span class="lead"></span><span>$ 38</span></div>
  <div class="sub" style="top:380px;letter-spacing:1.5px;right:28px">2LB Choice of Shrimp/Clams/Mussel/Crawfish</div>
  <div class="row tight" style="top:402px"><span>P3. Snow Crab plate</span><span class="lead"></span><span>$ 58</span></div>
  <div class="sub" style="top:418px">1LB Snow Crab and 1LB Choice of Shrimp/Clams/Mussel/Crawfish</div>

  <h2 style="top:446px">Family Meals</h2>
  <div class="row tight" style="top:479px"><span>M1. Seafood Combo 3 LB (1 flavor)</span><span class="lead"></span><span>$ 60</span></div>
  <div class="sub" style="top:494px">Choice of Shrimp/Clams/Mussel/Crawfish, ½ LB Sausage, 2 Corns, 2 Potato,</div>
  <div class="sub" style="top:504px">2 Eggs, (2cups) Fountain Soda (Substitute 1LB for Snow Crab + 20)</div>
  <div class="row tight" style="top:523px"><span>M2. Snow Crab Deluxe 4 LB (1 flavor)</span><span class="lead"></span><span>$ 130</span></div>
  <div class="sub" style="top:537px">6 Clusters of Snow Crab (3LB), 1LB choice of Shrimp/Clams/Mussel/Crawfish,</div>
  <div class="sub" style="top:547px">1LB Sausage, 4 Corns, 4 Potato, 4 Eggs, (2cups) Fountain Soda</div>

  <h2 style="top:572px">Choose Your Flavor</h2>
  <div class="center" style="top:603px;word-spacing:3px">Cajun (Classic), Garlic Butter,<br>Lemmon Papper, Skipper's Bomb</div>

  <h2 style="top:647px;left:-12px">Spice it up</h2>
  <div class="center" style="top:677px">Non-Spicy / Mild / Medium /Hot</div>

  <h2 style="top:702px;left:-12px">Drinks</h2>
  <div class="center" style="top:733px">Cola/Diet Cola/Zero Cola/Lemon-Lime<br>20oz Fountain (Free Refill) 3</div>
</section>

</body>
</html>
```